Harlow Vance Law Stationary - logo provided

I need Stationary designed for my Law Firm named Harlow Vance Law.

I have attached the firm's logo and would like that color and logos incorporated into the stationary. I need the stationary to look clean, simple and professional.

I need letterheads, envelopes and business cards designed. I would also like a letterhead version for 5.5 x 8..5 paper size (for handout printing)

Industry/Entity Type

Legal

```html
<!DOCTYPE html>
<html lang="en">
<head>
<meta charset="utf-8">
<title>Harlow Vance Law — Letterhead</title>
<link rel="stylesheet" href="https://fonts.googleapis.com/css2?family=Cinzel:wght@600&display=swap">
<style>
  :root {
    --maroon: #7a1f22;
    --gold: #c9a15a;
    --gold-light: #ead9b4;
    --paper: #ffffff;
    --watermark: #f2efea;
  }
  html, body {
    margin: 0;
    padding: 0;
    width: 849px;
    height: 1200px;
    overflow: hidden;
    background: var(--paper);
  }
  .letterhead {
    position: relative;
    width: 849px;
    height: 1200px;
    background: var(--paper);
    overflow: hidden;
    font-family: "Cinzel", serif;
    font-weight: 600;
  }
  .brand-name {
    position: absolute;
    margin: 0;
    color: var(--maroon);
    letter-spacing: 0.06em;
    white-space: nowrap;
    line-height: 1;
  }
  .brand-name--header {
    top: 50px;
    left: 50%;
    transform: translateX(-50%);
    font-size: 38px;
  }
  .brand-name--footer {
    left: 16px;
    top: 1074px;
    font-size: 16px;
  }
  .brand-name--watermark {
    top: 565px;
    left: 50%;
    transform: translateX(-50%);
    font-size: 44px;
    color: var(--watermark);
  }
  .band {
    position: absolute;
    left: 0;
    width: 849px;
    height: 36px;
  }
  .band--header {
    top: 150px;
    background: linear-gradient(90deg, var(--maroon) 0%, var(--maroon) 40%, var(--gold-light) 72%, var(--gold) 100%);
    opacity: 0.9;
  }
  .band--footer {
    top: 1124px;
    background: linear-gradient(90deg, var(--gold) 0%, var(--gold-light) 35%, var(--maroon) 68%, var(--maroon) 100%);
    opacity: 0.9;
  }
</style>
</head>
<body>
  <main class="letterhead">
    <p class="brand-name brand-name--header">Harlow Vance Law</p>
    <div class="band band--header" role="img" aria-label="Curved maroon and gold header band"></div>

    <p class="brand-name brand-name--watermark" aria-hidden="true">Harlow Vance Law</p>

    <p class="brand-name brand-name--footer">Harlow Vance Law</p>
    <div class="band band--footer" role="img" aria-label="Curved gold and maroon footer band"></div>
  </main>
</body>
</html>
```